Tello Haulage Junk Removal Postcard

I am looking to have a postcard made for my junk removal company. Details:
size: 6"x9"
I would like to keep it clean and simple. Our company colors are pink, blue and white. You can find the colors and info on the company and what we do on our website which is www.tellohaulage.example .
I've attached a sample of a postcard that was made on ArtHive for another junk removal company. I like the way the attached one looks.

```html
<!DOCTYPE html>
<html lang="en">
<head>
<meta charset="utf-8">
<title>Tello Haulage Postcard</title>
<link rel="stylesheet" href="https://fonts.googleapis.com/css2?family=Poppins:wght@300;400;500;600;700&family=Montserrat:wght@600;700;800&family=Oswald:wght@600&display=swap">
<style>
  :root {
    --blue: #2b5bea;
    --blue-deep: #0a2eb0;
    --blue-mid: #1d47d6;
    --pink: #ff1fd0;
    --red: #d9161d;
    --red-dark: #a80f14;
    --white: #ffffff;
    --ink: #111111;
    --stage: #dfe2e1;
    --stamp: #eef0f0;
  }
  * { margin: 0; padding: 0; box-sizing: border-box; }
  html, body { width: 1200px; height: 1200px; overflow: hidden; background: var(--stage); }
  .stage { position: relative; width: 1200px; height: 1200px; }
  .card {
    position: absolute; left: 255px; width: 690px; height: 460px;
    background: var(--white); overflow: hidden;
    font-family: "Poppins", sans-serif;
  }
  .card--front { top: 110px; }
  .card--back { top: 610px; }
  .card__art { position: absolute; inset: 0; width: 690px; height: 460px; }
  .abs { position: absolute; }

  /* brand name */
  .brand { display: flex; align-items: center; gap: 8px; white-space: nowrap; }
  .brand__dot { width: 16px; height: 16px; border-radius: 50%; background: var(--pink); flex: none; }
  .brand__name { font-family: "Poppins", sans-serif; font-weight: 700; color: var(--blue); line-height: 1; }
  .brand--front { left: 30px; top: 44px; }
  .brand--front .brand__name { font-size: 28px; }
  .brand--back { left: 462px; top: 52px; gap: 6px; }
  .brand--back .brand__name { font-size: 15px; }
  .brand--back .brand__dot { width: 9px; height: 9px; }

  /* ribbon */
  .badge { left: 242px; top: 100px; width: 154px; text-align: center; color: var(--white); font-family: "Oswald", sans-serif; font-weight: 600; line-height: 1; }
  .badge__big { font-size: 32px; display: block; }
  .badge__small { font-size: 15px; display: block; margin-top: 3px; letter-spacing: .5px; }

  /* headline */
  .headline { left: 31px; top: 122px; font-family: "Poppins", sans-serif; line-height: 44px; color: var(--white); font-size: 46px; }
  .headline__light { font-weight: 300; display: block; }
  .headline__bold { font-weight: 700; display: block; }
  .headline__accent { color: var(--pink); }

  .tagline-row { left: 31px; top: 286px; font-family: "Montserrat", sans-serif; font-weight: 700; font-size: 13px; color: var(--ink); }
  .tagline-row span { color: var(--pink); }

  .services { left: 31px; top: 318px; width: 300px; height: 80px; }
  .service { position: absolute; display: flex; align-items: center; gap: 10px; font-size: 12.5px; font-weight: 500; color: var(--ink); }
  .service svg { width: 27px; height: 27px; }
  .service--residential { left: 0; top: 0; }
  .service--commercial { left: 0; top: 44px; }
  .service--outside { left: 170px; top: 1px; }
  .service--curbside { left: 170px; top: 44px; }
  .services__divider { position: absolute; left: 141px; top: 2px; width: 1px; height: 70px; background: #d9d9d9; }

  .call { left: 29px; top: 425px; color: var(--white); font-size: 14px; font-weight: 300; display: flex; align-items: baseline; gap: 12px; }
  .call strong { font-family: "Montserrat", sans-serif; font-weight: 700; font-size: 19px; }
  .visit { left: 356px; top: 431px; color: var(--white); font-size: 14px; font-weight: 300; display: flex; align-items: baseline; gap: 10px; }
  .visit strong { font-family: "Montserrat", sans-serif; font-weight: 700; font-size: 14px; letter-spacing: 1px; }

  /* back */
  .story { left: 31px; top: 18px; width: 335px; color: var(--white); }
  .story__title { font-size: 17px; font-weight: 600; line-height: 22px; margin-bottom: 3px; }
  .story__title span { color: var(--pink); }
  .story p { font-size: 6.8px; line-height: 10.6px; margin-bottom: 10.6px; font-weight: 400; }

  .promise { left: 29px; top: 373px; color: var(--white); font-size: 11px; font-weight: 600; line-height: 14px; }
  .promise span { color: var(--pink); display: block; }
  .checks { left: 31px; top: 412px; width: 270px; height: 30px; }
  .check { position: absolute; display: flex; align-items: center; gap: 5px; color: var(--white); font-family: "Montserrat", sans-serif; font-weight: 700; font-size: 7.5px; }
  .check svg { width: 10px; height: 8px; }

  .stamp { left: 594px; top: 27px; width: 63px; height: 58px; background: var(--stamp); }

  .contact { top: 427px; display: flex; align-items: center; gap: 7px; color: var(--white); font-family: "Montserrat", sans-serif; font-weight: 700; white-space: nowrap; }
  .contact svg { width: 16px; height: 16px; flex: none; }
  .contact--phone { left: 340px; font-size: 14px; }
  .contact--web { left: 490px; font-size: 9.5px; letter-spacing: 0; }
  .contact--web svg { width: 14px; height: 14px; }
</style>
</head>
<body>
<div class="stage">

  <!-- FRONT -->
  <section class="card card--front">
    <svg class="card__art" viewBox="0 0 690 460">
      <defs>
        <linearGradient id="g-reno" x1="0" y1="0" x2="1" y2="1">
          <stop offset="0" stop-color="#e9e6df"/><stop offset=".5" stop-color="#b9a58c"/><stop offset="1" stop-color="#6e5a44"/>
        </linearGradient>
        <linearGradient id="g-garage" x1="0" y1="0" x2="1" y2="0">
          <stop offset="0" stop-color="#2b2b2b"/><stop offset=".35" stop-color="#d9341f"/><stop offset=".6" stop-color="#3a3a3a"/><stop offset="1" stop-color="#3f8a2f"/>
        </linearGradient>
        <linearGradient id="g-door" x1="0" y1="0" x2="1" y2="0">
          <stop offset="0" stop-color="#e8e8e8"/><stop offset=".3" stop-color="#2a2a2a"/><stop offset=".5" stop-color="#f2d21a"/><stop offset=".7" stop-color="#2a2a2a"/><stop offset="1" stop-color="#dcdcdc"/>
        </linearGradient>
      </defs>
      <polygon points="0,102 418,102 369,266 0,266" fill="var(--blue)"/>
      <polygon role="img" aria-label="Photo of a house interior being renovated" points="462,0 690,0 690,155 415,155" fill="url(#g-reno)"/>
      <polygon role="img" aria-label="Photo of a red garage door beside a tree" points="414,159 690,159 690,290 374,290" fill="url(#g-garage)"/>
      <polygon role="img" aria-label="Photo of a yellow front door behind black railings" points="372,296 690,296 690,412 335,412" fill="url(#g-door)"/>
      <line x1="452" y1="0" x2="419" y2="100" stroke="var(--pink)" stroke-width="2.5"/>
      <polygon points="0,412 322,412 307,460 0,460" fill="var(--pink)"/>
      <polygon points="328,423 690,423 690,460 316,460" fill="var(--blue)"/>
      <path d="M240,104 Q242,94 252,94 L386,94 Q396,94 398,104 Z" fill="var(--red-dark)"/>
      <path d="M254,98 L384,98 L380,146 Q318,158 258,146 Z" fill="var(--red)"/>
    </svg>

    <div class="abs brand brand--front">
      <span class="brand__name">Tello Haulage</span>
      <span class="brand__dot"></span>
    </div>

    <div class="abs badge">
      <span class="badge__big">24/7</span>
      <span class="badge__small">SERVICE</span>
    </div>

    <h1 class="abs headline">
      <span class="headline__light">RELAX.</span>
      <span class="headline__bold headline__accent">WE DO THE</span>
      <span class="headline__bold">DIRTY WORK</span>
    </h1>

    <p class="abs tagline-row">Remove The Junk <span>Reclaim Your Space</span></p>

    <div class="abs services">
      <div class="service service--residential">
        <svg viewBox="0 0 28 28" fill="none" stroke="var(--blue)" stroke-width="1.3"><path d="M3 13 L14 4 L25 13"/><path d="M6 11 V24 H22 V11"/><rect x="11" y="16" width="6" height="8"/><line x1="1" y1="24.5" x2="27" y2="24.5"/></svg>
        Residential
      </div>
      <div class="service service--commercial">
        <svg viewBox="0 0 28 28" fill="none" stroke="var(--blue)" stroke-width="1.3"><rect x="4" y="8" width="9" height="17"/><rect x="13" y="3" width="11" height="22"/><path d="M16 7h2M20 7h1M16 11h2M20 11h1M16 15h2M20 15h1M16 19h2M20 19h1M6 12h2M6 16h2M6 20h2"/></svg>
        Commercial
      </div>
      <div class="services__divider"></div>
      <div class="service service--outside">
        <svg viewBox="0 0 28 28" fill="none" stroke="var(--blue)" stroke-width="1.3"><circle cx="9" cy="10" r="5"/><line x1="9" y1="15" x2="9" y2="25"/><path d="M16 25 V18 H24 V25"/><path d="M18 7 a3 3 0 0 1 6 0 h2"/><line x1="2" y1="25" x2="27" y2="25"/></svg>
        Outside
      </div>
      <div class="service service--curbside">
        <svg viewBox="0 0 28 28" fill="none" stroke="var(--blue)" stroke-width="1.3"><rect x="2" y="8" width="15" height="12" rx="1"/><path d="M17 11 H22 L26 15 V20 H17"/><circle cx="7" cy="21" r="2.5"/><circle cx="21" cy="21" r="2.5"/></svg>
        Curbside
      </div>
    </div>

    <p class="abs call">Call or text <strong>555-014-2288</strong></p>
    <p class="abs visit">Visit Us: <strong>www.tellohaulage.example</strong></p>
  </section>

  <!-- BACK -->
  <section class="card card--back">
    <svg class="card__art" viewBox="0 0 690 460">
      <defs>
        <linearGradient id="g-bags" x1="0" y1="0" x2="0" y2="1">
          <stop offset="0" stop-color="#9a8f86"/><stop offset=".6" stop-color="#5d6a78"/><stop offset="1" stop-color="#3c8f5a"/>
        </linearGradient>
        <linearGradient id="g-skip" x1="0" y1="0" x2="0" y2="1">
          <stop offset="0" stop-color="#6d7478"/><stop offset=".25" stop-color="#c8ec2c"/><stop offset="1" stop-color="#a7cf16"/>
        </linearGradient>
        <radialGradient id="g-nest" cx=".5" cy=".5" r=".6">
          <stop offset="0" stop-color="#4a3f2a"/><stop offset=".45" stop-color="#8c8540"/><stop offset="1" stop-color="#f1e61e"/>
        </radialGradient>
      </defs>
      <polygon points="0,0 430,0 301,460 0,460" fill="var(--blue-deep)"/>
      <polygon points="0,232 365,232 330,356 0,356" fill="var(--blue-mid)"/>
      <line x1="438" y1="0" x2="411" y2="95" stroke="var(--pink)" stroke-width="2.5"/>
      <polygon points="322,415 690,415 690,460 309,460" fill="var(--pink)"/>
      <polygon role="img" aria-label="Photo of rubbish bags piled under a wall sign" points="19,244 130,244 146,342 34,342" fill="url(#g-bags)" stroke="var(--pink)" stroke-width="1"/>
      <polygon role="img" aria-label="Photo of a lime green skip container" points="135,244 247,244 262,342 152,342" fill="url(#g-skip)" stroke="var(--pink)" stroke-width="1"/>
      <polygon role="img" aria-label="Photo of a tangle of dry twigs on yellow" points="251,245 363,245 380,344 267,344" fill="url(#g-nest)" stroke="var(--pink)" stroke-width="1"/>
    </svg>

    <div class="abs story">
      <h2 class="story__title"><span>MEET</span> THE TELLOS</h2>
      <p>Born and raised in Alexandria, VA, Marco pursued higher education at Harborview University (HVU) in Boston where he majored in psychology - picking up what would become mission critical interpersonal skills for helping others manage stressful situations and working through difficult decisions.</p>
      <p>The greatest win, however, was meeting his wife, Elena, at HVU where she secured both her undergraduate and masters degree in higher education. After graduation, the duo moved down south to Charleston, SC and started a life for themselves through two ventures - Swift Lane Movers in 2010 and Swift Lane Junk in 2011.</p>
      <p>Despite loving the lowcountry life and building flourishing businesses, the Tellos felt called back to their roots and extended family - parents, siblings, cousins and more - in Northern Virginia after having two kids of their own, Leo and Nico.</p>
      <p>When the Tello's aren't out clearing out junk or hauling away clutter, you'll likely find them exploring new trails with their two kiddos.</p>
    </div>

    <p class="abs promise">WHATEVER YOU'RE UNDER, WE'RE HERE TO <span>HELP CLEAN IT OUT.</span></p>

    <div class="abs checks">
      <div class="check" style="left:0;top:0"><svg viewBox="0 0 10 8"><path d="M1 4 L4 7 L9 1" fill="none" stroke="var(--pink)" stroke-width="1.4"/></svg>trash</div>
      <div class="check" style="left:0;top:13px"><svg viewBox="0 0 10 8"><path d="M1 4 L4 7 L9 1" fill="none" stroke="var(--pink)" stroke-width="1.4"/></svg>hogwash</div>
      <div class="check" style="left:76px;top:0"><svg viewBox="0 0 10 8"><path d="M1 4 L4 7 L9 1" fill="none" stroke="var(--pink)" stroke-width="1.4"/></svg>Junk</div>
      <div class="check" style="left:76px;top:13px"><svg viewBox="0 0 10 8"><path d="M1 4 L4 7 L9 1" fill="none" stroke="var(--pink)" stroke-width="1.4"/></svg>clutter</div>
      <div class="check" style="left:141px;top:1px"><svg viewBox="0 0 10 8"><path d="M1 4 L4 7 L9 1" fill="none" stroke="var(--pink)" stroke-width="1.4"/></svg>debris</div>
      <div class="check" style="left:141px;top:14px"><svg viewBox="0 0 10 8"><path d="M1 4 L4 7 L9 1" fill="none" stroke="var(--pink)" stroke-width="1.4"/></svg>rubbish</div>
      <div class="check" style="left:206px;top:1px"><svg viewBox="0 0 10 8"><path d="M1 4 L4 7 L9 1" fill="none" stroke="var(--pink)" stroke-width="1.4"/></svg>garbage</div>
      <div class="check" style="left:206px;top:14px"><svg viewBox="0 0 10 8"><path d="M1 4 L4 7 L9 1" fill="none" stroke="var(--pink)" stroke-width="1.4"/></svg>scrap</div>
    </div>

    <div class="abs brand brand--back">
      <span class="brand__name">Tello Haulage</span>
      <span class="brand__dot"></span>
    </div>
    <div class="abs stamp"></div>

    <p class="abs contact contact--phone">
      <svg viewBox="0 0 16 16" fill="none" stroke="var(--white)" stroke-width="1.2"><path d="M3 1.5 L6 1.5 L7 5 L5.2 6.4 Q6.5 9.5 9.6 10.8 L11 9 L14.5 10 L14.5 13 Q14.5 14.5 13 14.5 Q1.5 13.5 1.5 3 Q1.5 1.5 3 1.5 Z"/></svg>
      555-014-2288
    </p>
    <p class="abs contact contact--web">
      <svg viewBox="0 0 16 16" fill="none" stroke="var(--white)" stroke-width="1.1"><circle cx="8" cy="8" r="6.5"/><ellipse cx="8" cy="8" rx="3" ry="6.5"/><line x1="1.5" y1="8" x2="14.5" y2="8"/><path d="M2.6 4.6 H13.4 M2.6 11.4 H13.4"/></svg>
      www.tellohaulage.example
    </p>
  </section>

</div>
</body>
</html>
```